Full Page Heron 250 Ad

We need a full page magazine ad. Our company is a site construction company - meaning we build lakes, ponds, do brush clearing for farmers and ranchers. For commercial customers, we build building pads, site clearing, pavement and soil stabilization. The final design should show what we do. Our website is www.dorvanlandworks.com

```html
<!DOCTYPE html>
<html lang="en">
<head>
<meta charset="utf-8">
<title>Dorvan Landworks – Full Page Ad</title>
<link href="https://fonts.googleapis.com/css2?family=Alfa+Slab+One&family=Anton&family=Poppins:wght@500;600;700&display=swap" rel="stylesheet">
<style>
  :root{
    --yellow:#f6b52e;
    --black:#111111;
    --charcoal:#262626;
    --white:#ffffff;
    --ink:#1c1c1c;
    --paper:#ffffff;
  }
  *{box-sizing:border-box;margin:0;padding:0}
  html,body{width:727px;height:1200px;overflow:hidden;background:var(--paper)}
  .ad{position:relative;width:727px;height:1200px;overflow:hidden;background:var(--paper);font-family:"Poppins",sans-serif}

  .hero-frame{position:absolute;left:0;top:0;width:727px;height:560px}
  .hero-photo{position:absolute;left:64px;top:0;width:663px;height:512px;border-bottom-left-radius:48px;
    background:
      radial-gradient(ellipse 38% 30% at 84% 30%, rgba(120,30,35,.85) 0%, rgba(120,30,35,0) 100%),
      radial-gradient(ellipse 55% 42% at 36% 48%, rgba(214,160,48,.95) 0%, rgba(214,160,48,0) 100%),
      radial-gradient(ellipse 30% 24% at 30% 82%, rgba(30,28,26,.8) 0%, rgba(30,28,26,0) 100%),
      radial-gradient(ellipse 25% 30% at 96% 8%, rgba(96,128,70,.8) 0%, rgba(96,128,70,0) 100%),
      linear-gradient(180deg,#cdbd9a 0%,#bba779 16%,#8e7a58 45%,#4c463f 72%,#35312d 100%)}
  .brand{position:absolute;right:50px;top:400px;display:flex;align-items:center;gap:10px;color:var(--white);
    font-family:"Poppins",sans-serif;font-weight:700;font-size:28px;letter-spacing:.3px}
  .brand-dot{width:18px;height:18px;border-radius:50%;background:var(--yellow)}

  .band{position:absolute;left:0;top:545px;width:727px;height:300px}
  .headline{position:absolute;left:0;top:598px;width:727px;text-align:center;color:var(--white);font-family:"Alfa Slab One",serif;text-transform:uppercase;font-weight:400}
  .headline .lead{font-size:31px;line-height:1}
  .headline .years{font-size:52px;color:var(--yellow);line-height:1}
  .headline .line2{display:block;font-size:31.5px;line-height:1.15;margin-top:2px}
  .intro{position:absolute;left:0;top:690px;width:727px;text-align:center;color:var(--white);font-size:18.5px;font-weight:500;line-height:1.2}

  .commercial-panel{position:absolute;left:363px;top:790px;width:364px;height:300px;background:var(--yellow)}

  .gallery{position:absolute;left:34px;top:812px;width:660px;height:160px;display:flex;gap:4px}
  .gallery-card{flex:1;border:5px solid var(--white);border-radius:14px;box-shadow:0 3px 8px rgba(0,0,0,.3)}
  .gallery-card.lake{background:
      radial-gradient(ellipse 40% 12% at 60% 42%, rgba(70,100,50,.9) 0%, rgba(70,100,50,0) 100%),
      linear-gradient(180deg,#7fa9cf 0%,#c3d3d6 34%,#6f7a47 46%,#7d6b4c 66%,#4f4232 100%)}
  .gallery-card.pad{background:
      radial-gradient(ellipse 45% 18% at 62% 28%, rgba(235,228,220,.95) 0%, rgba(235,228,220,0) 100%),
      radial-gradient(ellipse 30% 14% at 35% 45%, rgba(160,60,55,.5) 0%, rgba(160,60,55,0) 100%),
      linear-gradient(180deg,#9fa874 0%,#c9c3b0 22%,#e4ded2 55%,#cbc1ae 100%)}
  .gallery-card.shore{background:
      radial-gradient(ellipse 22% 14% at 58% 52%, rgba(170,35,40,.85) 0%, rgba(170,35,40,0) 100%),
      linear-gradient(180deg,#86b6e0 0%,#5e9290 30%,#6f8a82 42%,#8c7b63 56%,#574535 100%)}

  .ranch-copy{position:absolute;left:0;top:990px;width:363px;text-align:center;color:var(--ink);font-size:24px;font-weight:500;line-height:1.12}
  .commercial-tag{position:absolute;left:405px;top:990px;width:285px;height:34px;border-radius:5px;background:var(--black);
    color:var(--white);font-weight:700;font-size:16.5px;display:flex;align-items:center;justify-content:center}
  .commercial-tag span{color:var(--yellow);margin-left:5px}
  .commercial-copy{position:absolute;left:390px;top:1034px;width:320px;color:var(--ink);font-size:16.5px;font-weight:500;line-height:1.15}

  .footer{position:absolute;left:0;top:1090px;width:727px;height:110px;background:var(--black)}
  .phone-box{position:absolute;left:33px;top:1100px;width:312px;height:100px;border-radius:14px 14px 0 0;background:var(--yellow);
    display:flex;align-items:center;justify-content:center;gap:14px}
  .phone-icon{width:40px;height:40px;border-radius:50%;background:var(--black);display:flex;align-items:center;justify-content:center}
  .phone-number{font-family:"Anton",sans-serif;font-size:44px;color:var(--black);letter-spacing:-.5px}
  .website{position:absolute;left:345px;top:1100px;width:382px;height:100px;display:flex;align-items:center;justify-content:center;gap:11px}
  .web-icon{width:30px;height:30px;border-radius:50%;background:var(--yellow);display:flex;align-items:center;justify-content:center;flex:none}
  .web-address{font-family:"Anton",sans-serif;font-size:31px;color:var(--white);letter-spacing:-.3px;white-space:nowrap}
</style>
</head>
<body>
<main class="ad">

  <svg class="hero-frame" viewBox="0 0 727 560" aria-hidden="true">
    <path d="M46 0 V468 Q46 528 106 528 H176" fill="none" stroke="var(--yellow)" stroke-width="16"/>
    <polygon points="182,520 206,520 198,536 174,536" fill="var(--black)"/>
    <polygon points="212,520 236,520 228,536 204,536" fill="var(--yellow)"/>
    <polygon points="242,520 266,520 258,536 234,536" fill="var(--black)"/>
    <polygon points="272,520 296,520 288,536 264,536" fill="var(--yellow)"/>
    <polygon points="306,520 727,520 727,536 298,536" fill="var(--black)"/>
  </svg>

  <div class="hero-photo" role="img" aria-label="Yellow earthmoving scraper pulled by a red four-wheel-drive tractor on a cleared dirt site"></div>
  <div class="brand"><span class="brand-dot"></span>Dorvan Landworks</div>

  <svg class="band" viewBox="0 0 727 300" preserveAspectRatio="none" aria-hidden="true">
    <defs>
      <linearGradient id="bandShade" x1="0" y1="0" x2="0" y2="1">
        <stop offset="0" stop-color="#242424"/>
        <stop offset="1" stop-color="#333333"/>
      </linearGradient>
    </defs>
    <path d="M0 22 L30 18 L60 24 L95 14 L130 20 L170 12 L210 19 L250 10 L300 17 L340 9 L390 16 L430 8 L480 15 L520 7 L570 14 L610 6 L660 12 L700 5 L727 9 V300 H0 Z" fill="url(#bandShade)"/>
  </svg>

  <h1 class="headline">
    <span class="lead">With over </span><span class="years">50 Years</span>
    <span class="line2">of experience in the industry,</span>
  </h1>
  <p class="intro">We have what it takes to help you develop your land for<br>your long or short term goals.</p>

  <div class="commercial-panel"></div>

  <div class="gallery">
    <div class="gallery-card lake" role="img" aria-label="Newly dug pond basin on ranch land with trees"></div>
    <div class="gallery-card pad" role="img" aria-label="Aerial view of a commercial building pad and parking lot"></div>
    <div class="gallery-card shore" role="img" aria-label="Tractor and scraper clearing a shoreline site by the water"></div>
  </div>

  <p class="ranch-copy">We build lakes • ponds •<br>do brush clearing for<br>farmers and ranchers.</p>

  <div class="commercial-tag">For commercial<span>customers,</span></div>
  <p class="commercial-copy">we build building pads •site clearing,<br>pavement and soil stabilization.</p>

  <footer class="footer"></footer>
  <div class="phone-box">
    <span class="phone-icon">
      <svg width="22" height="22" viewBox="0 0 24 24" aria-hidden="true"><path fill="var(--yellow)" d="M6.6 10.8c1.4 2.8 3.8 5.1 6.6 6.6l2.2-2.2c.3-.3.7-.4 1-.2 1.1.4 2.3.6 3.6.6.6 0 1 .4 1 1V20c0 .6-.4 1-1 1C10.6 21 3 13.4 3 4c0-.6.4-1 1-1h3.5c.6 0 1 .4 1 1 0 1.3.2 2.5.6 3.6.1.3 0 .7-.2 1z"/></svg>
    </span>
    <span class="phone-number">361.555-0148</span>
  </div>
  <div class="website">
    <span class="web-icon">
      <svg width="20" height="20" viewBox="0 0 24 24" aria-hidden="true" fill="none" stroke="var(--black)" stroke-width="1.8"><circle cx="12" cy="12" r="9"/><path d="M3 12h18M12 3c3 3.5 3 14.5 0 18M12 3c-3 3.5-3 14.5 0 18"/></svg>
    </span>
    <span class="web-address">DORVANLANDWORKS.COM</span>
  </div>

</main>
</body>
</html>
```